Kestrel Summit 2019 Enemies of the End-Times Church Flyer

We want a church conference flyer designed. We are looking for a professional, yet catchy design that uses our brand colors and logo creatively while communicating key information of the event effectively. <br/>The flyer must include all of the following:<br/>Title: Kestrel Summit 2019<br/>Topic: The Enemies of The End-Times Church <br/>Subtitles: <br/> -How the antichrist raises an army by social behavior engineering. <br/>-How the architects of modern social constructs escaped the church's radar. <br/>-The Holy Spirit's end-times agenda:<br/> The Knock-Out Punch!<br/>Speaker: Prophet Marcus Toliver <br/>Dates/time: December 27, 28 & 29 at 6pm<br/>Location: Halvorn Community Center <br/> 241 Pellham Street <br/> Portland, ME 04102<br/>Contact info: phone: 207-555-0148 <br/>email: contact@brookmeadow.example <br/> www.vutel.example<br/>*The flyer must also include a picture of the speaker and our Vutel logo <br/>Thanks, we look forward to seeing what you come up with!

Colors

Designer to choose colors to be used in the design.

Requirements
Must have
• The flyer must include all of the following:
• Title: Kestrel Summit 2019
• Topic: The Enemies of The End-Times Church
• Subtitles:
• -How the antichrist raises an army by social behavior engineering.
• -How the architects of modern social constructs escaped the church's radar.
• -The Holy Spirit's end-times agenda:
• The Knock-Out Punch!
• Speaker: Prophet Marcus Toliver
• Dates/time: December 27, 28 & 29 at 6pm
• Location: Halvorn Community Center
• 241 Pellham Street
• Portland, ME 04102
• Contact info: phone: 207-555-0148
• email: contact@brookmeadow.example
• www.vutel.example
• *The flyer must also include a picture of the speaker and our Vutel logo
Should not have
• Pictures of crosses or church buildings

```html
<!DOCTYPE html>
<html lang="en">
<head>
<meta charset="utf-8">
<title>Kestrel Summit 2019 Flyer</title>
<link href="https://fonts.googleapis.com/css2?family=Montserrat:wght@400;500;600;700;800&display=swap" rel="stylesheet">
<style>
  :root {
    --orange: #f29a1f;
    --navy: #0d2259;
    --ink: #2c3036;
    --paper: #e4e5e7;
    --white: #ffffff;
  }
  html, body { margin: 0; padding: 0; overflow: hidden; }
  body { width: 1116px; height: 1200px; background: var(--paper); font-family: "Montserrat", sans-serif; }
  .flyer { position: relative; width: 1116px; height: 1200px; overflow: hidden; background: linear-gradient(160deg, #eeeff1 0%, #dcdde0 100%); }
  .speaker-photo { position: absolute; left: 0; top: 0; width: 1116px; height: 960px;
    background: radial-gradient(ellipse at 52% 30%, #6e6e70 0%, #8d8d8f 30%, #b8b8ba 65%, #cfcfd1 100%); }
  .shapes { position: absolute; left: 0; top: 0; }
  .logo { position: absolute; right: 40px; top: 20px; width: 126px; height: 96px; background: var(--white);
    display: flex; align-items: center; justify-content: center; font-weight: 600; font-size: 28px; color: var(--navy); }
  .event-title { position: absolute; left: 34px; top: 282px; border-left: 11px solid var(--orange); padding-left: 28px; }
  .event-title .name { display: block; font-weight: 800; font-size: 46px; color: var(--navy); line-height: 1.05; letter-spacing: 1px; }
  .event-title .kind { display: block; font-weight: 700; font-size: 28px; color: var(--white); letter-spacing: 2px; margin-top: 6px; }
  .event-title .year { display: block; font-weight: 800; font-size: 58px; color: var(--navy); line-height: 1.1; margin-top: 4px; }
  .band-text { position: absolute; left: 112px; top: 612px; transform: rotate(-17deg); transform-origin: 0 0; width: 1100px; }
  .topic { font-weight: 700; font-size: 32px; color: var(--white); letter-spacing: 2px; white-space: nowrap; }
  .speaker { position: relative; margin-top: 8px; height: 150px; }
  .speaker .role { position: absolute; left: -12px; top: 104px; transform: rotate(-90deg); transform-origin: 0 0; font-weight: 700; font-size: 15px; color: var(--white); letter-spacing: 2px; }
  .speaker .title { position: absolute; left: 72px; top: 2px; font-weight: 800; font-size: 26px; color: var(--white); letter-spacing: 1px; }
  .speaker .person { position: absolute; left: 22px; top: 22px; font-weight: 800; font-size: 100px; color: var(--ink); white-space: nowrap; line-height: 1.1; }
  .dates { margin-left: 110px; font-weight: 700; font-size: 44px; color: var(--white); letter-spacing: 2px; white-space: nowrap; }
  .venue { position: absolute; left: 640px; top: 752px; }
  .venue .place { font-weight: 700; font-size: 23px; color: var(--ink); letter-spacing: 1px; }
  .venue .phone { font-weight: 800; font-size: 50px; color: var(--navy); letter-spacing: 3px; margin-top: 2px; }
  .points { position: absolute; list-style: none; margin: 0; padding: 0; }
  .points li { border-left: 6px solid var(--orange); padding-left: 20px; font-size: 21px; font-weight: 500; color: var(--ink); line-height: 1.3; margin-bottom: 26px; }
  .points.left { left: 60px; top: 948px; width: 420px; }
  .points.right { left: 640px; top: 878px; width: 440px; }
  .footer { position: absolute; left: 0; bottom: 0; width: 1116px; height: 138px; background: var(--navy); }
  .contact { position: absolute; display: grid; grid-template-columns: auto auto; column-gap: 16px; row-gap: 6px; align-items: baseline; }
  .contact dt { font-weight: 700; font-size: 18px; color: var(--orange); text-align: right; margin: 0; }
  .contact dd { font-weight: 500; font-size: 22px; color: var(--white); margin: 0; line-height: 1.25; }
  .contact.site { left: 190px; top: 30px; }
  .contact.reach { left: 640px; top: 22px; }
</style>
</head>
<body>
<div class="flyer">
  <div class="speaker-photo" role="img" aria-label="Black and white portrait of the speaker in front of bookshelves"></div>

  <svg class="shapes" width="1116" height="1200" viewBox="0 0 1116 1200" aria-hidden="true">
    <polygon points="0,960 1116,620 1116,1200 0,1200" fill="#e1e2e5"/>
    <polygon points="0,1060 1116,760 1116,1200 0,1200" fill="#ebecee"/>
    <polygon points="0,620 1116,279 1116,579 0,920" fill="#f29a1f"/>
  </svg>

  <div class="logo">Vutel</div>

  <h1 class="event-title">
    <span class="name">KESTREL</span>
    <span class="kind">SUMMIT</span>
    <span class="year">2019</span>
  </h1>

  <div class="band-text">
    <div class="topic">THE ENEMIES OF THE END-TIMES CHURCH</div>
    <div class="speaker">
      <span class="role">SPEAKER</span>
      <span class="title">PROPHET</span>
      <span class="person">Marcus Toliver</span>
    </div>
    <div class="dates">DECEMBER 27, 28 &amp; 29 AT 6PM</div>
  </div>

  <div class="venue">
    <div class="place">HALVORN COMMUNITY CENTER</div>
    <div class="phone">207-555-0148</div>
  </div>

  <ul class="points left">
    <li>How the antichrist raises an army by social behavior engineering.</li>
    <li>The Holy Spirit's end-times agenda.</li>
  </ul>
  <ul class="points right">
    <li>How the architects of modern social constructs escaped the church's radar.</li>
    <li>The Knock-Out Punch!</li>
  </ul>

  <footer class="footer">
    <dl class="contact site">
      <dt>WEBSITE :</dt><dd>www.vutel.example</dd>
      <dt>ADDRESS:</dt><dd>241 Pellham Street<br>Portland, ME 04102</dd>
    </dl>
    <dl class="contact reach">
      <dt>PHONE:</dt><dd>207-555-0148</dd>
      <dt>EMAIL :</dt><dd>contact@brookmeadow.example</dd>
    </dl>
  </footer>
</div>
</body>
</html>
```